Modern Lawfirm Business Card Design

We're looking for a business card to incorporate the newly created logo we had made.

Ideally looking for a law firm business card demonstrating, modern, minimalist, strong/bold design.

I'm open to any design honestly, but nothing "flashy".

Target Market(s)

Immigration law, family immigration, humanitarian, general legal

Industry/Entity Type

Law Firm

Contact Information for Business Card

Please use dummy information, name, street address, city, state, phone number, email, website.

Font styles to use
Serif
Sans Serif

Requirements
Must have
• Please use dummy information, name, street address, city, state, phone number, email, website.

```html
<!DOCTYPE html>
<html lang="en">
<head>
<meta charset="utf-8">
<title>Calder Immigration Law — Business Card</title>
<link rel="stylesheet" href="https://fonts.googleapis.com/css2?family=Libre+Baskerville:wght@700&family=Open+Sans:wght@400&display=swap">
<style>
  :root {
    --navy: #1f4a8a;
    --navy-deep: #183d75;
    --white: #ffffff;
    --backdrop: #1d1d1f;
  }
  * { margin: 0; padding: 0; box-sizing: border-box; }
  html, body {
    width: 1200px;
    height: 1000px;
    overflow: hidden;
    background: var(--backdrop);
  }
  .canvas {
    position: relative;
    width: 1200px;
    height: 1000px;
  }
  .card {
    position: absolute;
    left: 280px;
    width: 640px;
    height: 366px;
    overflow: hidden;
  }
  .card--front {
    top: 84px;
    background: var(--navy);
    display: flex;
    align-items: center;
    justify-content: center;
  }
  .card--back {
    top: 530px;
    background: var(--white);
  }
  .wordmark {
    display: flex;
    align-items: center;
    gap: 14px;
    font-family: "Libre Baskerville", Georgia, serif;
    font-weight: 700;
    font-size: 30px;
    letter-spacing: 1px;
  }
  .wordmark__square {
    width: 22px;
    height: 22px;
  }
  .card--front .wordmark { color: var(--white); }
  .card--front .wordmark__square { background: var(--white); }
  .card--back .wordmark {
    position: absolute;
    top: 70px;
    left: 0;
    right: 0;
    justify-content: center;
    color: var(--navy);
  }
  .card--back .wordmark__square { background: var(--navy); }
  .card__band {
    position: absolute;
    left: 0;
    bottom: 0;
    width: 640px;
    height: 178px;
  }
  .holder {
    position: absolute;
    left: 50px;
    bottom: 40px;
    color: var(--white);
    font-family: "Libre Baskerville", Georgia, serif;
    font-weight: 700;
  }
  .holder__name { font-size: 24px; line-height: 1.3; }
  .holder__title { font-size: 16px; line-height: 1.4; }
  .contact {
    position: absolute;
    right: 46px;
    bottom: 40px;
    color: var(--white);
    font-family: "Open Sans", Arial, sans-serif;
    font-size: 14px;
    line-height: 1.45;
  }
  .contact__address { margin-bottom: 8px; }
  .contact__row {
    display: flex;
    align-items: center;
    gap: 10px;
  }
  .contact__icon { width: 12px; height: 12px; flex: none; }
</style>
</head>
<body>
<main class="canvas">

  <section class="card card--front" aria-label="Card front">
    <div class="wordmark">
      <span class="wordmark__square"></span>
      <span class="wordmark__name">Calder Immigration Law</span>
    </div>
  </section>

  <section class="card card--back" aria-label="Card back">
    <div class="wordmark">
      <span class="wordmark__square"></span>
      <span class="wordmark__name">Calder Immigration Law</span>
    </div>

    <svg class="card__band" viewBox="0 0 640 178" aria-hidden="true">
      <path d="M0 30 H120 L140 0 V30 H640 V178 H0 Z" fill="var(--navy)"/>
    </svg>

    <div class="holder">
      <p class="holder__name">Daniel Reyes</p>
      <p class="holder__title">Founder/CEO</p>
    </div>

    <div class="contact">
      <p class="contact__address">Your Street Address,<br>Singapore, 123</p>
      <p class="contact__row">
        <svg class="contact__icon" viewBox="0 0 12 12" aria-hidden="true"><path d="M2.5 1 L4.5 1 L5.3 3.4 L4 4.4 Q5 6.8 7.6 8 L8.6 6.7 L11 7.5 L11 9.5 Q10 11 8.5 11 Q1 9.5 1 3 Q1 1.6 2.5 1 Z" fill="var(--white)"/></svg>
        000 111 2223
      </p>
      <p class="contact__row">
        <svg class="contact__icon" viewBox="0 0 12 12" aria-hidden="true"><rect x="0.5" y="2.5" width="11" height="7.5" fill="var(--white)"/><path d="M0.8 2.8 L6 6.8 L11.2 2.8" fill="none" stroke="var(--navy)" stroke-width="1"/></svg>
        urname@email.com
      </p>
      <p class="contact__row">
        <svg class="contact__icon" viewBox="0 0 12 12" aria-hidden="true"><circle cx="6" cy="6" r="5.2" fill="none" stroke="var(--white)" stroke-width="1.2"/><ellipse cx="6" cy="6" rx="2.2" ry="5.2" fill="none" stroke="var(--white)" stroke-width="1"/><path d="M1 6 H11" stroke="var(--white)" stroke-width="1"/></svg>
        www.sitename.com
      </p>
    </div>
  </section>

</main>
</body>
</html>
```